professional business card

Professional business card with logo on one side, and underneath logo list:
- power
-data
-fibre optic
-isolar

On other side:
Marcus Trent
Owner
MOB 0492 738 204
marcus@vorpa.com.au
www.vorpaelectrical.com.au

Please edit logo to just leave VORPA

```html
<!DOCTYPE html>
<html lang="en">
<head>
<meta charset="utf-8">
<title>VORPA Business Card</title>
<link rel="stylesheet" href="https://fonts.googleapis.com/css2?family=Roboto:wght@400;500;700;900&display=swap">
<style>
  :root {
    --teal: #089fa2;
    --teal-dark: #07878a;
    --paper: #e3e3e3;
    --ink: #555758;
    --ink-soft: #6d6f70;
    --stage: #3b3c3f;
    --ring: #5a5a5a;
    --black: #111;
    --white: #ffffff;
  }
  * { box-sizing: border-box; margin: 0; padding: 0; }
  html, body {
    width: 1200px; height: 1200px; overflow: hidden;
    background: var(--stage);
    font-family: "Roboto", Arial, sans-serif;
  }
  .canvas {
    position: relative; width: 1200px; height: 1200px;
    display: flex; flex-direction: column; align-items: center; justify-content: center; gap: 60px;
  }
  .card {
    position: relative; width: 900px; height: 515px;
    border-radius: 34px; overflow: hidden;
  }

  /* Front */
  .card--front { background: var(--teal); color: var(--white); }
  .front-brand {
    position: absolute; top: 110px; left: 0; right: 0; text-align: center;
    font-weight: 900; font-size: 150px; letter-spacing: 6px; line-height: 1;
  }
  .services {
    position: absolute; top: 320px; left: 0; right: 0;
    display: flex; justify-content: center; gap: 62px; list-style: none;
  }
  .service { width: 110px; display: flex; flex-direction: column; align-items: center; }
  .service__badge {
    width: 100px; height: 100px; border-radius: 50%;
    background: var(--teal); border: 7px solid var(--ring);
    box-shadow: 0 0 0 2px var(--black);
    display: flex; align-items: center; justify-content: center;
  }
  .service__badge svg { width: 62px; height: 62px; }
  .service__label {
    margin-top: 14px; font-weight: 700; font-size: 19px; text-align: center; line-height: 1.05;
    text-transform: uppercase;
  }

  /* Back */
  .card--back { background: var(--paper); }
  .back-wave { position: absolute; left: 0; bottom: 0; width: 900px; height: 515px; }
  .back-brand {
    position: absolute; top: 172px; left: 70px; width: 350px; text-align: center;
    font-weight: 900; font-size: 86px; letter-spacing: 2px; color: var(--teal); line-height: 1;
  }
  .divider {
    position: absolute; top: 120px; left: 455px; width: 3px; height: 190px; background: var(--teal);
  }
  .contact { position: absolute; top: 132px; left: 490px; }
  .contact__name { font-weight: 700; font-size: 40px; color: var(--teal); line-height: 1; }
  .contact__role { font-size: 22px; color: var(--ink-soft); margin-top: 4px; }
  .contact__list { list-style: none; margin-top: 26px; }
  .contact__item {
    display: flex; align-items: center; gap: 12px;
    font-size: 27px; font-weight: 500; color: var(--ink); line-height: 1.3;
  }
  .contact__item svg { width: 22px; height: 22px; flex: none; }
  .contact__item .accent { color: var(--teal); }
</style>
</head>
<body>
<main class="canvas">

  <section class="card card--front" aria-label="Card front">
    <h1 class="front-brand">VORPA</h1>
    <ul class="services">
      <li class="service">
        <span class="service__badge">
          <svg viewBox="0 0 64 64" fill="none" stroke="#fff" stroke-width="4">
            <circle cx="32" cy="32" r="24"/>
            <path d="M36 10 L20 36 H32 L27 56 L46 28 H34 Z" fill="#fff" stroke="none"/>
          </svg>
        </span>
        <span class="service__label">Power</span>
      </li>
      <li class="service">
        <span class="service__badge">
          <svg viewBox="0 0 64 64" fill="none" stroke="#fff" stroke-width="3.5">
            <ellipse cx="32" cy="14" rx="20" ry="7"/>
            <path d="M12 14 V50 C12 54 21 57 32 57 C43 57 52 54 52 50 V14"/>
            <path d="M12 26 C12 30 21 33 32 33 C43 33 52 30 52 26"/>
            <path d="M12 38 C12 42 21 45 32 45 C43 45 52 42 52 38"/>
          </svg>
        </span>
        <span class="service__label">Data</span>
      </li>
      <li class="service">
        <span class="service__badge">
          <svg viewBox="0 0 64 64" fill="none" stroke="#fff" stroke-width="2.5">
            <circle cx="32" cy="32" r="26"/>
            <path d="M12 18 C26 26 36 36 42 48"/>
            <path d="M16 12 C30 22 40 32 48 42"/>
            <path d="M24 9 C36 18 46 28 54 34"/>
            <circle cx="42" cy="48" r="2.5" fill="#fff"/>
            <circle cx="48" cy="42" r="2.5" fill="#fff"/>
            <circle cx="54" cy="34" r="2.5" fill="#fff"/>
          </svg>
        </span>
        <span class="service__label">Optic<br>Fibre</span>
      </li>
      <li class="service">
        <span class="service__badge">
          <svg viewBox="0 0 64 64" fill="none" stroke="#fff" stroke-width="2.5">
            <path d="M8 48 L18 26 H46 L40 48 Z"/>
            <path d="M13 37 H43 M26 26 L22 48 M36 26 L32 48"/>
            <circle cx="50" cy="16" r="5"/>
            <path d="M50 5 V8 M50 24 V27 M39 16 H42 M58 16 H61 M42 8 L44 10 M56 22 L58 24 M58 8 L56 10"/>
          </svg>
        </span>
        <span class="service__label">Isolar</span>
      </li>
    </ul>
  </section>

  <section class="card card--back" aria-label="Card back">
    <svg class="back-wave" viewBox="0 0 900 515" preserveAspectRatio="none" aria-hidden="true">
      <path d="M0 385 C120 370 240 380 400 430 C560 480 700 470 900 455 V515 H0 Z" fill="var(--black)"/>
      <path d="M0 400 C120 385 240 395 400 445 C560 495 700 485 900 470 V515 H0 Z" fill="var(--teal)"/>
    </svg>
    <div class="back-brand">VORPA</div>
    <span class="divider"></span>
    <div class="contact">
      <p class="contact__name">Marcus Trent</p>
      <p class="contact__role">Owner</p>
      <ul class="contact__list">
        <li class="contact__item">
          <svg viewBox="0 0 24 24" fill="var(--teal)"><path d="M6.6 10.8a15 15 0 0 0 6.6 6.6l2.2-2.2a1 1 0 0 1 1-.25 11.4 11.4 0 0 0 3.6.6 1 1 0 0 1 1 1V20a1 1 0 0 1-1 1A17 17 0 0 1 3 4a1 1 0 0 1 1-1h3.5a1 1 0 0 1 1 1c0 1.25.2 2.45.6 3.6a1 1 0 0 1-.25 1z"/></svg>
          <span>0492 738 204</span>
        </li>
        <li class="contact__item">
          <svg viewBox="0 0 24 24" fill="none" stroke="var(--teal)" stroke-width="2"><rect x="2" y="5" width="20" height="14" rx="1"/><path d="M2 6 L12 13 L22 6"/></svg>
          <span>marcus@vorpa.com.au</span>
        </li>
        <li class="contact__item">
          <svg viewBox="0 0 24 24" fill="none" stroke="var(--teal)" stroke-width="1.8"><circle cx="12" cy="12" r="10"/><path d="M2 12 H22 M12 2 C15 5 15 19 12 22 M12 2 C9 5 9 19 12 22"/></svg>
          <span>www.<span class="accent">vorpaelectrical</span>.com.au</span>
        </li>
      </ul>
    </div>
  </section>

</main>
</body>
</html>
```